Solar energy proposal for homeowners

I am providing households with solar energy proposals, and I need a high-quality brochure that is packaged cleverly to attract the homeowner's attention. Take a look at the one page solar brochure that I have included to get an idea of text and content.

Target Market(s)

Residential Homeowners

Industry/Entity Type

Solar

Requirements
Must have
• High quality document

```html
<!DOCTYPE html>
<html lang="en">
<head>
<meta charset="utf-8">
<title>Brightfield Energy – Solar for $0 Down</title>
<link href="https://fonts.googleapis.com/css2?family=Poppins:wght@400;500;600;700&family=Titan+One&display=swap" rel="stylesheet">
<style>
  :root {
    --canvas: #3b3946;
    --paper: #ffffff;
    --teal: #12a6cf;
    --cyan: #0aa6d6;
    --green: #12c41a;
    --lime: #86d24a;
    --navy: #0b2466;
    --ink: #0d2a5e;
  }
  * { margin: 0; padding: 0; box-sizing: border-box; }
  html, body { width: 1200px; height: 1200px; overflow: hidden; background: var(--canvas); }
  body { position: relative; font-family: "Poppins", sans-serif; }

  .flyer {
    position: absolute; left: 190px; top: 20px;
    width: 820px; height: 1160px;
    background: var(--paper); overflow: hidden;
  }
  .flyer-shapes { position: absolute; inset: 0; width: 820px; height: 1160px; }

  .house-visual {
    position: absolute; left: 60px; top: 30px; width: 446px; height: 510px;
    border-radius: 18px;
    background: linear-gradient(180deg, #4d5868 0%, #7a6048 38%, #a57a4f 58%, #5f7f45 82%, #3f6a34 100%);
  }

  .brand {
    position: absolute; right: 28px; top: 44px;
    display: flex; align-items: center; gap: 12px;
  }
  .brand-mark { width: 40px; height: 40px; border-radius: 50%; background: var(--teal); }
  .brand-name { font-family: "Poppins", sans-serif; font-weight: 500; font-size: 32px; color: var(--teal); line-height: 1; letter-spacing: -0.5px; }

  .headline {
    position: absolute; left: 516px; top: 154px; width: 300px;
    font-family: "Titan One", sans-serif; font-size: 45px; line-height: 41.5px;
    color: var(--cyan); text-transform: uppercase;
    text-shadow: 2px 2px 0 rgba(11,36,102,0.18);
  }
  .tagline {
    position: absolute; left: 516px; top: 327px; width: 290px;
    font-weight: 600; font-size: 16px; line-height: 18px; color: var(--navy);
  }

  .section-title { font-family: "Titan One", sans-serif; font-size: 31px; color: var(--navy); line-height: 1; position: absolute; }
  .about-title { left: 512px; top: 416px; }
  .about-text {
    position: absolute; left: 512px; top: 455px; width: 282px;
    font-weight: 500; font-size: 12.8px; line-height: 16.6px; color: #1b1b1b;
  }
  .why-title { left: 120px; top: 582px; }

  .pill {
    position: absolute; height: 37px; border-radius: 19px;
    background: var(--cyan); color: #fff;
    font-weight: 500; font-size: 12.5px;
    display: flex; align-items: center; gap: 7px; padding-left: 12px;
  }
  .pill svg { width: 20px; height: 20px; flex: none; }

  .service-box {
    position: absolute; left: 32px; top: 771px; width: 506px; height: 337px;
    border: 4px solid #fff; border-radius: 20px;
    background: linear-gradient(100deg, var(--teal) 0%, #3cbfa0 55%, var(--lime) 100%);
    box-shadow: 0 0 0 1px rgba(0,0,0,0.04);
  }
  .service-title { left: 67px; top: 809px; }
  .feature { position: absolute; width: 165px; }
  .feature.right { width: 150px; }
  .feature-icon {
    position: absolute; left: -61px; top: -4px; width: 46px; height: 46px;
    border-radius: 50%; background: var(--green); border: 3px solid #0d7f5a;
    display: flex; align-items: center; justify-content: center;
  }
  .feature-icon svg { width: 24px; height: 24px; }
  .feature-title { font-weight: 600; font-size: 15px; line-height: 16.5px; color: #0e3a93; }
  .feature-text { margin-top: 7px; font-weight: 600; font-size: 11px; line-height: 13.3px; color: var(--navy); }

  .panel-visual {
    position: absolute; left: 552px; top: 832px; width: 252px; height: 244px;
    border-radius: 16px;
    background: linear-gradient(145deg, #6a98e6 0%, #2a5cc4 45%, #143a8e 100%);
  }

  .contact { position: absolute; top: 1120px; display: flex; align-items: center; gap: 8px; font-weight: 500; font-size: 12.5px; line-height: 14px; color: #111; }
  .contact-icon { width: 29px; height: 29px; border-radius: 50%; border: 2px solid var(--green); display: flex; align-items: center; justify-content: center; background: #fff; }
  .contact-icon svg { width: 15px; height: 15px; }
  .contact-phone { left: 251px; }
  .contact-address { left: 404px; }
  .contact-web { left: 564px; }
</style>
</head>
<body>
<main class="flyer">
  <svg class="flyer-shapes" viewBox="0 0 820 1160" aria-hidden="true">
    <defs>
      <linearGradient id="edgeGrad" x1="0" y1="0" x2="1" y2="0">
        <stop offset="0" stop-color="#12a6cf"/>
        <stop offset="0.55" stop-color="#1fb0b8"/>
        <stop offset="1" stop-color="#7fd06a"/>
      </linearGradient>
      <linearGradient id="footGrad" x1="0" y1="0" x2="1" y2="0">
        <stop offset="0" stop-color="#12a6cf"/>
        <stop offset="0.6" stop-color="#6fcd55"/>
        <stop offset="1" stop-color="#a4dc2a"/>
      </linearGradient>
    </defs>
    <path d="M0 0 H125 C62 240 40 520 80 780 L80 1120 L0 1120 Z" fill="url(#edgeGrad)"/>
    <path d="M0 1100 H220 L262 1160 H0 Z" fill="url(#footGrad)"/>
    <path d="M178 0 H198 C140 250 112 520 122 770 L108 770 C98 520 122 250 178 0 Z" fill="#12c41a"/>
    <path d="M784 0 H820 V115 C805 70 795 35 784 0 Z" fill="#12c41a"/>
    <path d="M820 800 C790 920 760 1050 712 1160 H820 Z" fill="#12c41a"/>
  </svg>

  <div class="house-visual" role="img" aria-label="Modern two-storey home with solar panels on the roof, surrounded by greenery"></div>

  <div class="brand">
    <span class="brand-mark"></span>
    <span class="brand-name">brightfield energy</span>
  </div>

  <h1 class="headline">Solar for<br>$0 down.<br>No liens.<br>No kidding.</h1>
  <p class="tagline">Power Your Future with Brightfield Energy</p>

  <h2 class="section-title about-title">About Us</h2>
  <p class="about-text">At Brightfield Energy, our mission is to make solar simple and accessible for everyone. No high-pressure sales–just the information you need to make a smart choice. With our solar rental program, you can lower your monthly energy costs and pay less than your current electricity bill.</p>

  <h2 class="section-title why-title">Why Choose Us?</h2>

  <div class="pill" style="left:120px;top:636px;width:147px;"><svg viewBox="0 0 20 20" fill="none" stroke="#fff" stroke-width="1.5"><circle cx="10" cy="10" r="8.5"/><path d="M4 16 L16 4"/></svg>No Financing</div>
  <div class="pill" style="left:277px;top:636px;width:109px;"><svg viewBox="0 0 20 20" fill="none" stroke="#fff" stroke-width="1.5"><circle cx="10" cy="10" r="8.5"/><path d="M4 16 L16 4"/></svg>No Liens</div>
  <div class="pill" style="left:397px;top:636px;width:175px;"><svg viewBox="0 0 20 20" fill="none" stroke="#fff" stroke-width="1.5"><rect x="2" y="5" width="16" height="10" rx="2"/><path d="M3 17 L17 3"/></svg>No Down Payment</div>
  <div class="pill" style="left:120px;top:685px;width:178px;"><svg viewBox="0 0 20 20" fill="none" stroke="#fff" stroke-width="1.5"><path d="M2 9 Q10 0 18 9 Z"/><path d="M10 9 V17"/></svg>No Insurance Costs</div>
  <div class="pill" style="left:308px;top:685px;width:230px;"><svg viewBox="0 0 20 20" fill="none" stroke="#fff" stroke-width="1.5"><rect x="3" y="2" width="12" height="16" rx="2"/><circle cx="13" cy="13" r="4"/></svg>No Long-Term Commitment</div>
  <div class="pill" style="left:548px;top:685px;width:195px;"><svg viewBox="0 0 20 20" fill="none" stroke="#fff" stroke-width="1.5"><circle cx="10" cy="10" r="4"/><circle cx="10" cy="10" r="8" stroke-dasharray="3 2"/></svg>No Maintenance Costs</div>

  <section class="service-box" aria-labelledby="service-heading"></section>
  <h2 class="section-title service-title" id="service-heading">Our Best Service</h2>

  <div class="feature" style="left:128px;top:873px;">
    <span class="feature-icon"><svg viewBox="0 0 24 24" fill="none" stroke="#0b2466" stroke-width="2"><circle cx="12" cy="12" r="9"/><path d="M15 8.5 C13 7 9 7.5 9.5 10 S15 12 14.5 14.5 S10.5 17 9 15.5 M12 5.5 V18.5"/></svg></span>
    <div class="feature-title">Affordable<br>&amp; Transparent</div>
    <p class="feature-text">Simple pricing, no hidden fees and a fixed monthly rate lower than typical energy bills.</p>
  </div>
  <div class="feature right" style="left:366px;top:873px;">
    <span class="feature-icon"><svg viewBox="0 0 24 24" fill="none" stroke="#0b2466" stroke-width="2"><path d="M12 21 C7 15 5 12 5 9 A7 7 0 0 1 19 9 C19 12 17 15 12 21 Z"/><circle cx="12" cy="9" r="2.5"/></svg></span>
    <div class="feature-title">Local<br>Expertise</div>
    <p class="feature-text">Florida-based team that understands the needs of Orlando and statewide homeowners.</p>
  </div>
  <div class="feature" style="left:128px;top:989px;">
    <span class="feature-icon"><svg viewBox="0 0 24 24" fill="none" stroke="#0b2466" stroke-width="2"><path d="M14.5 4 A4.5 4.5 0 0 0 10 10 L4 16 L7 19 L13 13 A4.5 4.5 0 0 0 19.5 8.5 L16.5 10 L14 8.5 Z"/></svg></span>
    <div class="feature-title">Expert<br>Installation</div>
    <p class="feature-text">Certified professionals handle installation, maintenance, and repairs end to end.</p>
  </div>
  <div class="feature right" style="left:366px;top:989px;">
    <span class="feature-icon"><svg viewBox="0 0 24 24" fill="none" stroke="#0b2466" stroke-width="2"><path d="M5 19 C5 10 11 5 19 5 C19 13 14 19 5 19 Z"/><path d="M5 19 L13 11"/></svg></span>
    <div class="feature-title">Eco-<br>Friendly</div>
    <p class="feature-text">Clean, renewable solar energy that helps reduce your carbon footprint.</p>
  </div>

  <div class="panel-visual" role="img" aria-label="Ground-mounted solar panel array on a metal frame"></div>

  <div class="contact contact-phone">
    <span class="contact-icon"><svg viewBox="0 0 16 16" fill="#111"><path d="M3.5 1.5 L6 1 L7.2 4.3 L5.6 5.6 C6.4 7.5 8.5 9.6 10.4 10.4 L11.7 8.8 L15 10 L14.5 12.5 C14 14 12.5 15 10.5 14.5 C6 13 3 10 1.5 5.5 C1 3.5 2 2 3.5 1.5 Z"/></svg></span>
    <span>(555)014-2290</span>
  </div>
  <div class="contact contact-address">
    <span class="contact-icon"><svg viewBox="0 0 16 16" fill="#111"><path d="M8 15 C4.5 10.5 3 8 3 6 A5 5 0 0 1 13 6 C13 8 11.5 10.5 8 15 Z M8 4 A2 2 0 1 0 8 8 A2 2 0 1 0 8 4 Z" fill-rule="evenodd"/></svg></span>
    <span>123 Anywhere St.,<br>Any City</span>
  </div>
  <div class="contact contact-web">
    <span class="contact-icon"><svg viewBox="0 0 16 16" fill="none" stroke="#111" stroke-width="1.4"><circle cx="8" cy="8" r="6.5"/><ellipse cx="8" cy="8" rx="3" ry="6.5"/><path d="M1.5 8 H14.5"/></svg></span>
    <span>www.brightfieldenergy.com</span>
  </div>
</main>
</body>
</html>
```